Web Design Project Bright Lane

I am needing a website for a theatre called Bright Lane Stage School (blstageschool.com) which has already been purchsed from web nook. (Let me know if you need any other info on that.)We need a website that is professional looking and easy to access. Attached is the logo as well as the business card design. I think it would be nice to have the same type of design that’s on the business card but I am definitely open to other creative ideas. I need the website to be in a format where I can edit it in the future when I need to add classes and events to it. Also, some other things I need are I need are a…
A homepage. On the homepage we would like the motto, “Rise to the spotlight.” Also, the mission statement,
Bright Lane Stage School strives to help students achieve excellence in performance, while building self-confidence and creativity. The Bright Lane Stage School has created a fun and safe environment, where students can learn, acquire new skills, and explore their potential through musical theatre. Students not only have the freedom to, but are encouraged to embrace who they are and can lose their fear of judgment from others.
Class Registration Page for the classes- (As well as a quick fund option for each if that is possible)
4-6 Musical Theatre
Tuesday’s 4:00PM-5:00PM
January 6th – February 24th
8 Weeks
Cost $160
Curriculum: Moss Kite
Class info: In MT 4-6 your students will learn the basics of singing, dancing, and acting. A lesson of theatre terminology or technique will be taught each week as well as working on the show that will be performed at the end of the 8 weeks semester.

6-9 Musical Theatre
Tuesday’s 5:15PM-6:45PM
January 6th- February 24th
8 Weeks
Cost: $200
Curriculum: Delia
Class info: In MT 6-9 your students will learn the basics of singing, dancing, and acting. A lesson of theatre terminology or technique will be taught each week as well as working on the show that will be performed at the end of the 8 weeks semester.
9-12 Musical Theatre
Wednesday’s 5:00-7:00PM
8 Weeks
Cost: $240
Curriculum: Gilded
Class info: In MT 9-12 your students will learn intermediate levels of singing, dancing, and acting. A lesson of theatre terminology or technique will be taught each week as well as working on the show that will be performed at the end of the 8 weeks semester.

About- (Include headshot that is attached)
A native Coloradan, Marisol is an actress, director, teacher, and wife. She was a Dean’s List graduate of Northvale College in Florida, she holds a B.S. degree in Theatre. Her Capstone Project involved writing, producing, directing, and starring in a 60-minute one-woman musical which was noted by the Chairman of Theatre as setting new standard for the NVC project. Initially attending Harrow Ridge College, Marisol was one of nine students representing HR at the Upper Plains Drama Festival. Marisol has also been a senior theatre director at the Willowmere Youth Playhouse for 4 years, where she directed fall, spring, and summer classes for ages 4-19. Her experience includes directing the main stage production, Quill Tr., assistant director for, Nobody Minds Old Tobias Grey, and stage management for Der Wandelstern.

Contact us
Phone: 555-214-7390
Email: blstageschoolhub.com

Also, I do not have any photos of students yet so it's ok if their aren't many pictures because I intend on adding some when things get going, so if it's simple that's great. Also, if you find any musical theatre pictures that don't include faces, are just bodies or feet, that would work as well.
Updates

The web address needs to be blstageschool.com. I have already purchased the domain name from WebNook. Let me know if there are any steps I might be missing or any other info I need to provide. Also, I need to be able to edit the website in the future but I'm not sure which format is best for that.

Target Market(s)

Theatre parents and students

Industry/Entity Type

Building

Requirements
Must have
• Stated above.

```html
<!DOCTYPE html>
<html lang="en">
<head>
<meta charset="utf-8">
<title>Bright Lane Stage School</title>
<link rel="stylesheet" href="https://fonts.googleapis.com/css2?family=Cormorant+Garamond:ital,wght@0,400;0,500;1,400&display=swap">
<style>
  :root {
    --brand-red: #a30f0f;
    --ink: #1a1a1a;
    --muted: #8a8a8a;
    --rule: #d6d6d6;
    --paper: #ffffff;
  }
  * { box-sizing: border-box; margin: 0; padding: 0; }
  html, body { width: 1200px; height: 1000px; overflow: hidden; background: var(--paper); }
  body {
    position: relative;
    font-family: "Cormorant Garamond", Georgia, serif;
    color: var(--ink);
    border-top: 4px solid var(--brand-red);
    border-bottom: 4px solid var(--brand-red);
  }
  .site-header {
    position: absolute; top: 28px; left: 0; width: 1200px; height: 100px;
  }
  .brand {
    position: absolute; left: 262px; top: 30px;
    display: flex; align-items: center; gap: 10px;
    font-size: 32px; font-weight: 500; color: var(--ink);
  }
  .brand-mark { width: 14px; height: 14px; background: var(--brand-red); }
  .main-nav { position: absolute; left: 617px; top: 38px; display: flex; gap: 49px; }
  .main-nav a {
    font-size: 24px; color: var(--muted); text-decoration: none; padding-bottom: 2px;
  }
  .main-nav a.is-current { color: var(--ink); border-bottom: 2px solid var(--brand-red); }
  .hero {
    position: absolute; left: 100px; top: 151px; width: 1000px; height: 218px;
    background: linear-gradient(180deg, #e9e6df 0%, #c8c6bd 22%, #7fa85a 40%, #6f9a4c 100%);
    display: flex; align-items: center; justify-content: center;
  }
  .hero-motto {
    font-style: italic; font-size: 48px; color: #fff;
    text-shadow: 0 2px 4px rgba(0,0,0,.45);
    position: relative; top: -10px;
  }
  .rule { position: absolute; left: 100px; width: 1000px; height: 1px; background: var(--rule); }
  .rule-top { top: 415px; }
  .rule-bottom { top: 841px; }
  .mission { position: absolute; left: 100px; top: 449px; width: 1000px; }
  .mission p { font-size: 27px; line-height: 30px; margin-bottom: 30px; }
  .mission .name { color: var(--brand-red); }
  .site-footer {
    position: absolute; left: 0; top: 900px; width: 1200px;
    display: flex; justify-content: center; align-items: center; gap: 10px;
    font-size: 32px; font-weight: 500;
  }
</style>
</head>
<body>
  <header class="site-header">
    <div class="brand"><span class="brand-mark"></span>Bright Lane</div>
    <nav class="main-nav">
      <a href="#" class="is-current">Home</a>
      <a href="#">Registration</a>
      <a href="#">About</a>
    </nav>
  </header>

  <section class="hero" role="img" aria-label="Photo of four students reading scripts together on a sunny lawn">
    <span class="hero-motto">“Rise to the spotlight.”</span>
  </section>

  <div class="rule rule-top"></div>

  <main class="mission">
    <p><span class="name">The Bright Lane Stage School</span> strives to help students achieve excellence in performance, while building self-confidence and creativity.</p>
    <p><span class="name">The Bright Lane Stage School</span> has created a fun and safe environment, where students can learn, acquire new skills, and explore their potential through musical theatre.</p>
    <p>Students not only have the freedom to, but are encouraged to embrace who they are and can lose their fear of judgment from others.</p>
  </main>

  <div class="rule rule-bottom"></div>

  <footer class="site-footer"><span class="brand-mark"></span>Bright Lane</footer>
</body>
</html>
```